Commercial Cleaning Company Website Design

We are working with Harbor Sweep Team. They are a commercial cleaning company that needs a new website design.

Some sites to use for inspiration:

https://www.plenvask.com
https://glint-panecleaning.com
https://tidyhelpers.net
https://calmnesthouse.com
https://www.thecleaningbureauxyz.com
https://www.dottiebroom.com

Thank you for taking the time to consider designing a website for us. We are web developers based in Stockton and Los Angeles, CA, USA. Most of our projects go through the same process. Understanding this process may help you win a project with us. We custom-code all of our websites in-house. We don’t have any requirements as to what tools you use for your design, but we prefer Figma files. For any design that we label as four-stars, we send it to the client for review. The client picks the final design they want us to use. Once we complete this process, we will continue to show additional clients all the four-star sites and purchase them later. Your designs will have multiple chances to sell. For better chances of success, we ask that you follow these guidelines.

IMAGES:
If you use any images or icons in the design, we ask that you have a link to the asset so we can purchase the image/icon. Most of the designs we submit do not have the customer’s images on them unless they have some great images. Be creative; show us the feeling you are trying to portray with your image choices. Use any royalty-free site you choose. We subscribe to Adobe and mainly use their images, but we can purchase images outside of Adobe.

PLEASE NOTE: we will not submit designs to clients with watermarks on the images.

FONTS:
We ask that you identify the fonts used in the design. This can be done in a message if you want. We typically use Google Fonts and Adobe Fonts.

CONTENT:
We're always open to different content and ideas. We often submit designs with stock images so the client can see our vision. We typically take pictures after the website launch to use their images with our vision. Lorem Ipsum is fine for paragraphs, but we ask that you write the headers in correct English. We want to be able to show the vision and identify the sections of the website.

INSPIRATION:
We typically add a couple of links in the brief of websites we like to help you get started in your design.

REVISIONS:
We do not often ask for revisions of the designs unless we see something in the design that may not appeal to the client. If there are slight changes that we want to make, we do that in the development process.

FEEDBACK:
We rarely give feedback on designs during the design process. We are working on many website projects and do not have the time to provide feedback. We usually respond if your request is well thought out and asks specific questions, but a note asking “feedback, please” usually goes unanswered.

```html
<!DOCTYPE html>
<html lang="en">
<head>
<meta charset="UTF-8">
<title>Harbor Sweep Team – Commercial Cleaning</title>
<link rel="stylesheet" href="https://fonts.googleapis.com/css2?family=Poppins:wght@500;600;700&family=Montserrat:wght@400;500;600;700&display=swap">
<style>
:root{
  --blue:#1f4fc8;
  --blue-dark:#1a3fa6;
  --red:#e8291f;
  --ink:#1b1b1b;
  --muted:#444;
  --soft:#f5f5f7;
  --soft-blue:#eef1fb;
  --footer:#1c1c1c;
}
*{box-sizing:border-box;margin:0;padding:0}
html,body{width:1200px;height:3091px;overflow:hidden}
body{font-family:"Montserrat",sans-serif;color:var(--ink);background:#fff;position:relative}
h1,h2,h3{font-family:"Poppins",sans-serif}
section,header{position:relative;width:1200px}
.abs{position:absolute}
.spark{position:absolute;width:18px;height:18px;z-index:3}
.spark.lg{width:30px;height:30px}

/* top bar */
.topbar{height:54px;background:var(--blue);color:#fff;display:flex;align-items:center;justify-content:flex-end;padding-right:104px;gap:50px}
.topbar .quote{font-size:22px;font-weight:500}
.topbar .phone{font-family:"Poppins",sans-serif;font-size:22px;font-weight:600}
.topbar .book{border:2px solid #fff;border-radius:6px;padding:6px 8px;font-size:13px;font-weight:600}

/* nav */
.nav{height:90px;display:flex;align-items:center;padding:0 104px;font-size:13.5px;font-weight:500}
.nav .links{display:flex;gap:34px;flex:1}
.nav .links.right{justify-content:flex-end}
.brand{display:flex;align-items:center;gap:8px;font-family:"Poppins",sans-serif;font-weight:600;color:var(--blue);font-size:17px;letter-spacing:.5px;white-space:nowrap}
.brand .dot{width:14px;height:14px;border-radius:50%;background:var(--red)}

/* hero */
.hero{height:490px}
.hero h1{left:104px;top:96px;width:520px;font-size:35px;line-height:46px;letter-spacing:-.2px;color:var(--blue);font-weight:700;white-space:nowrap;z-index:2}
.hero .lead{left:104px;top:254px;width:240px;font-size:13.5px;line-height:23px;color:var(--muted);font-weight:500}
.btn{display:inline-flex;align-items:center;justify-content:center;font-weight:700;font-size:13px;border-radius:5px}
.btn.solid{background:var(--red);color:#fff}
.btn.outline{border:2px solid var(--blue);color:var(--blue)}
.hero .b1{left:104px;top:340px;width:149px;height:44px}
.hero .b2{left:272px;top:340px;width:149px;height:44px}
.hero .photo{left:440px;top:0;width:760px;height:490px;background:linear-gradient(120deg,#dfe6ea 0%,#b7c7cf 35%,#3a6fd6 60%,#2457c9 80%,#cfd8de 100%);clip-path:path("M30 0 H760 V490 H125 Q-40 330 30 0 Z");z-index:1}

/* issues */
.issues{height:552px;background:var(--soft)}
.tile{position:absolute;width:220px;height:183px;border-radius:16px;overflow:hidden}
.tile .label{position:absolute;bottom:0;background:#fff;font-size:13px;font-weight:600;padding:8px 10px 4px}
.tile .label.l{left:0;border-top-right-radius:12px}
.tile .label.r{right:0;border-top-left-radius:12px}
.issues h2{left:608px;top:82px;font-size:38px;color:var(--blue);font-weight:700}
.issues .ribbon{left:608px;top:144px;width:488px;height:69px;background:var(--red);color:#fff;font-family:"Poppins",sans-serif;font-weight:700;font-size:36px;display:flex;align-items:center;justify-content:center;border-radius:10px 0 10px 0;white-space:nowrap}
.issues p{left:608px;top:228px;width:490px;font-size:13.5px;line-height:23.4px;color:var(--muted)}
.issues .more{left:608px;top:364px;width:149px;height:45px;background:var(--blue);color:#fff}

/* clients */
.clients{height:554px}
.center-title{position:absolute;left:0;right:0;text-align:center;font-size:38px;font-weight:700;color:var(--blue)}
.clients .center-title{top:46px}
.review{position:absolute;top:138px;width:318px;height:350px;border:1px solid #ddd;border-radius:12px;background:#fff;box-shadow:0 10px 14px -8px rgba(31,79,200,.35);padding:42px 24px 0}
.review p{font-size:15px;line-height:23.5px;color:#333;height:188px}
.stars{display:flex;gap:11px;margin:2px 0 22px 2px}
.stars svg{width:22px;height:22px}
.who{display:flex;align-items:center;gap:10px}
.who .avatar{width:40px;height:40px;border-radius:50%;background:linear-gradient(#c9d2dc,#8e9aa8)}
.who b{display:block;font-size:15px;font-weight:600}
.who span{font-size:12.5px;color:#444}
.arrow{position:absolute;top:302px;width:22px;height:22px;border-radius:50%;background:var(--red);z-index:2}

/* services */
.services{height:906px;background:var(--soft-blue)}
.services .center-title{top:78px}
.card{position:absolute;width:318px;height:328px;border-radius:14px;padding:0 22px;color:#fff;overflow:hidden}
.card.red{background:linear-gradient(160deg,#ef5a4d,#e0372c)}
.card.blue{background:linear-gradient(160deg,#4a74d8,#2b57c4)}
.card h3{margin-top:84px;font-size:23px;line-height:27px;font-weight:600}
.card p{margin-top:10px;font-size:15px;line-height:19px}
.card .learn{position:absolute;left:22px;bottom:18px;width:148px;height:41px;border:2px solid #fff;border-radius:6px;display:flex;align-items:center;justify-content:center;gap:12px;font-weight:600;font-size:15px}

/* find */
.find{height:282px;background:linear-gradient(90deg,#2450c4 0%,#3e4ab0 60%,#8f3a6d 100%)}
.find .panel{left:103px;top:40px;width:989px;height:206px;background:#fff;border-radius:16px;overflow:hidden}
.find .map{left:0;top:0;width:485px;height:206px;background:linear-gradient(135deg,#eef1f4,#d9e8d8 55%,#f3e6cf)}
.find h2{left:505px;top:22px;font-size:31px;font-weight:700}
.find .sub{left:505px;top:78px;font-size:15px;color:#333}
.find .field{left:505px;top:111px;width:448px;height:46px;border:1.5px solid #222;border-radius:8px;display:flex;align-items:center;overflow:hidden}
.find .field .ph{flex:1;display:flex;align-items:center;gap:12px;padding-left:14px;font-size:13px;color:#bbb}
.find .field .go{width:160px;height:100%;background:#111;color:#fff;display:flex;align-items:center;justify-content:center;font-size:14px;font-weight:600}
.find .call{left:505px;top:166px;font-size:19px;font-weight:700}

/* footer */
.footer{height:120px;background:var(--footer);color:#bbb;display:flex;align-items:center;padding:0 104px 0 110px}
.footer .brand{color:#ddd;font-size:15px;margin-right:54px}
.footer nav{display:flex;gap:26px;font-size:13.5px;flex:1}
.footer .contact{color:#fff;width:140px}
.footer .contact small{display:block;font-size:13px;line-height:15px}
.footer .contact strong{display:block;font-size:19px;font-weight:500;margin:2px 0 8px}
.socials{display:flex;gap:18px}
.socials i{width:18px;height:18px;border-radius:3px;background:#888;display:block}
.copyright{height:43px;background:var(--footer);border-top:1px solid #333;color:#888;font-size:13px;display:flex;align-items:center;justify-content:center}
</style>
</head>
<body>
<svg width="0" height="0" style="position:absolute">
  <defs>
    <symbol id="star4" viewBox="0 0 20 20"><path d="M10 0 C11 7 13 9 20 10 C13 11 11 13 10 20 C9 13 7 11 0 10 C7 9 9 7 10 0Z"/></symbol>
    <symbol id="star5" viewBox="0 0 24 24"><path d="M12 1.5l3.1 6.9 7.4.7-5.6 5 1.7 7.4L12 17.7 5.4 21.5l1.7-7.4-5.6-5 7.4-.7z"/></symbol>
  </defs>
</svg>

<header class="topbar">
  <span class="quote">Get a custom quote today</span>
  <span class="phone">555-010-2468</span>
  <span class="book">BOOK NOW</span>
</header>

<header class="nav">
  <div class="links"><span>About Us</span><span>Why Hire Us?</span><span>Our Service</span></div>
  <div class="brand"><span class="dot"></span>Harbor Sweep Team</div>
  <div class="links right"><span>Careers</span><span>Cleaning Tips</span><span>Find A location</span></div>
</header>

<section class="hero">
  <svg class="spark" style="left:124px;top:64px;fill:var(--blue)"><use href="#star4"/></svg>
  <svg class="spark" style="left:403px;top:80px;fill:var(--red)"><use href="#star4"/></svg>
  <svg class="spark lg" style="left:360px;top:196px;fill:var(--blue)"><use href="#star4"/></svg>
  <h1 class="abs">Professional Commercial<br>Cleaning Services You<br>Can Trust</h1>
  <p class="abs lead">Let Harbor Sweep Team Make Your Home Shine!</p>
  <span class="abs btn solid b1">GET PRICING</span>
  <span class="abs btn outline b2">CALL US</span>
  <div class="abs photo" role="img" aria-label="Two smiling cleaners in blue shirts holding a spray bottle and squeegee in an office"></div>
</section>

<section class="issues">
  <div class="tile" style="left:103px;top:84px;background:linear-gradient(135deg,#d9d4cc,#6fb9d9)" role="img" aria-label="Gloved hand scrubbing bathroom tiles"><span class="label l">Bathrooms</span></div>
  <div class="tile" style="left:340px;top:84px;background:linear-gradient(135deg,#ece6de,#b9a996)" role="img" aria-label="Cleaners tidying a living room"><span class="label l">Living Room</span></div>
  <div class="tile" style="left:103px;top:286px;background:linear-gradient(135deg,#8a8f93,#cfd3d6)" role="img" aria-label="Clean stainless kitchen sink and tap"><span class="label r">Kitchens</span></div>
  <div class="tile" style="left:340px;top:286px;background:linear-gradient(135deg,#bfd2d8,#d6c4ad)" role="img" aria-label="Neat bedroom with made bed"><span class="label r">Sleeping Areas</span></div>
  <svg class="spark" style="left:858px;top:52px;fill:var(--red)"><use href="#star4"/></svg>
  <svg class="spark lg" style="left:574px;top:124px;width:24px;height:24px;fill:var(--blue)"><use href="#star4"/></svg>
  <svg class="spark" style="left:974px;top:116px;width:12px;height:12px;fill:var(--blue)"><use href="#star4"/></svg>
  <h2 class="abs">Cleaning Issues?</h2>
  <div class="abs ribbon">We’ve Got the Solution!</div>
  <p class="abs">At Harbor Sweep Team, we focus on solving your toughest cleaning challenges from everyday messes to deep, hard-to-reach grime. Our thorough cleaning approach ensures your home stays fresh, spotless, and sanitized from corner to corner.</p>
  <span class="abs btn more">More About Us</span>
</section>

<section class="clients">
  <svg class="spark" style="left:633px;top:20px;fill:var(--red)"><use href="#star4"/></svg>
  <svg class="spark" style="left:342px;top:82px;width:22px;height:22px;fill:var(--blue)"><use href="#star4"/></svg>
  <svg class="spark" style="left:824px;top:82px;fill:#c8cbd3"><use href="#star4"/></svg>
  <h2 class="center-title">Hear From Our Clients</h2>
  <span class="arrow" style="left:92px"></span>
  <article class="review" style="left:103px">
    <p>Our office has never looked this clean! Harbor Sweep Team has been incredibly consistent, professional, and detail-oriented. They take care of everything – even the small corners we always forget about</p>
    <div class="stars"><svg fill="#e8291f"><use href="#star5"/></svg><svg fill="#e8291f"><use href="#star5"/></svg><svg fill="#e8291f"><use href="#star5"/></svg><svg fill="#e8291f"><use href="#star5"/></svg><svg fill="#e8291f"><use href="#star5"/></svg></div>
    <div class="who"><span class="avatar"></span><div><b>Daniel K</b><span>Office Manager, Stockton</span></div></div>
  </article>
  <article class="review" style="left:440px">
    <p>I love coming home after their visit – everything feels fresh, organized, and spotless. The team is friendly, trustworthy, and always goes the extra mile. Highly recommended!</p>
    <div class="stars"><svg fill="#e8291f"><use href="#star5"/></svg><svg fill="#e8291f"><use href="#star5"/></svg><svg fill="#e8291f"><use href="#star5"/></svg><svg fill="#e8291f"><use href="#star5"/></svg><svg fill="#e8291f"><use href="#star5"/></svg></div>
    <div class="who"><span class="avatar"></span><div><b>Priya M</b><span>Homeowner, Los Angeles</span></div></div>
  </article>
  <article class="review" style="left:779px">
    <p>We’ve worked with several cleaning companies before, but none match the reliability of Harbor Sweep Team. They don’t just clean – they genuinely care about our space and our staff’s comfort.</p>
    <div class="stars"><svg fill="#e8291f"><use href="#star5"/></svg><svg fill="#e8291f"><use href="#star5"/></svg><svg fill="#e8291f"><use href="#star5"/></svg><svg fill="#e8291f"><use href="#star5"/></svg><svg fill="#e8291f"><use href="#star5"/></svg></div>
    <div class="who"><span class="avatar"></span><div><b>Helen T</b><span>Facilities Director</span></div></div>
  </article>
  <span class="arrow" style="left:1086px"></span>
</section>

<section class="services">
  <svg class="spark" style="left:405px;top:52px;fill:var(--red)"><use href="#star4"/></svg>
  <svg class="spark" style="left:150px;top:112px;fill:var(--blue)"><use href="#star4"/></svg>
  <svg class="spark" style="left:622px;top:134px;fill:#c8cbd3"><use href="#star4"/></svg>
  <svg class="spark lg" style="left:1022px;top:108px;fill:var(--blue)"><use href="#star4"/></svg>
  <h2 class="center-title">Professional Cleaning Services We Offer</h2>

  <article class="card red" style="left:103px;top:170px" role="img" aria-label="Office cleaning photo tinted red">
    <h3>Office Cleaning</h3><p>Daily maintenance and deep cleaning for professional office spaces.</p>
    <span class="learn">Learn More →</span>
  </article>
  <article class="card blue" style="left:440px;top:170px" role="img" aria-label="Window cleaning photo tinted blue">
    <h3 style="margin-top:80px">Window &amp; Glass Cleaning</h3><p>Crystal-clear windows and glass surfaces for a polished appearance.</p>
    <span class="learn" style="bottom:26px">Learn More →</span>
  </article>
  <article class="card red" style="left:779px;top:170px" role="img" aria-label="Carpet cleaning photo tinted red">
    <h3>Floor &amp; Carpet Care</h3><p>Professional floor maintenance and carpet cleaning services.</p>
    <span class="learn">Learn More →</span>
  </article>
  <article class="card blue" style="left:103px;top:528px" role="img" aria-label="Janitorial worker photo tinted blue">
    <h3>Janitorial Services</h3><p>Comprehensive janitorial services for ongoing facility maintenance.</p>
    <span class="learn">Learn More →</span>
  </article>
  <article class="card red" style="left:440px;top:528px" role="img" aria-label="Moving van photo tinted red">
    <h3>Move-In / Move-Out Cleaning</h3><p>Complete cleaning for transitions and new occupancy.</p>
    <span class="learn">Learn More →</span>
  </article>
  <article class="card blue" style="left:779px;top:528px" role="img" aria-label="Post-construction cleanup photo tinted blue">
    <h3>Post-Construction Cleaning</h3><p>Specialized cleaning after construction or renovation projects.</p>
    <span class="learn">Learn More →</span>
  </article>
</section>

<section class="find">
  <div class="abs panel">
    <div class="abs map" role="img" aria-label="Map with location pins"></div>
    <h2 class="abs">Find Harbor Sweep Team</h2>
    <p class="abs sub">Let us know how we can help you today</p>
    <div class="abs field">
      <span class="ph"><svg width="16" height="20" viewBox="0 0 16 20"><path d="M8 0a7 7 0 0 0-7 7c0 5 7 13 7 13s7-8 7-13a7 7 0 0 0-7-7zm0 10a3 3 0 1 1 0-6 3 3 0 0 1 0 6z" fill="#111"/></svg>Enter Zip /Postal Code</span>
      <span class="go">Find A Location</span>
    </div>
    <p class="abs call">Call us at 555-010-2468</p>
  </div>
</section>

<footer class="footer">
  <div class="brand"><span class="dot" style="background:#ddd;width:10px;height:10px"></span>Harbor Sweep Team</div>
  <nav><span>About Us</span><span>Why Hire Us?</span><span>Our Service</span><span>Careers</span><span>Cleaning Tips</span><span>Find A location</span></nav>
  <div class="contact">
    <small>Call now for a free estimate!</small>
    <strong>555-010-2468</strong>
    <div class="socials"><i></i><i></i><i></i><i></i></div>
  </div>
</footer>
<div class="copyright">© 2025 Harbor Sweep Team. All rights reserved.</div>
</body>
</html>
```